Birchwell Agency Condominium mail merge

We need a marketing proposal letter design to do a mail merge to potential e customers. We included our logo and an example of my miserable attempt to create a template. We are looking for a modern and attractive proposal template. Here is our website https://www.birchwellagency.example to be used for any additional information needed about us and our services.

Target Market(s)

New prospects

Industry/Entity Type

Insurance Agency

Requirements
Must have
• My project must have a modern professional look with merge fields similar to the file uploaded with this project.
Nice to have
• it would like have a condominium and a car icon graphic depicting there is additional discounts for both quotes bundled.
Should not have
• My project should not have any other logos or company name

```html
<!DOCTYPE html>
<html lang="en">
<head>
<meta charset="utf-8">
<title>Birchwell Agency Letterhead</title>
<link href="https://fonts.googleapis.com/css2?family=Source+Sans+3:wght@400;600;700&family=Arimo:wght@700&display=swap" rel="stylesheet">
<style>
  :root {
    --green: #3db54a;
    --orange: #f47c20;
    --text: #777777;
    --heading: #444444;
    --dark: #333333;
    --paper: #ffffff;
    --backdrop: #e6e6e6;
  }
  * { box-sizing: border-box; margin: 0; padding: 0; }
  html, body { width: 1059px; height: 1200px; overflow: hidden; }
  body {
    background: var(--backdrop);
    font-family: "Source Sans 3", sans-serif;
    position: relative;
  }
  .letter {
    position: absolute;
    left: 121px; top: 24px;
    width: 816px; height: 1152px;
    background: linear-gradient(#ffffff 0%, #f7f7f7 75%, #ffffff 100%);
  }
  .brand {
    position: absolute; left: 65px; top: 70px;
    display: flex; align-items: center; gap: 10px;
  }
  .brand-mark { width: 22px; height: 22px; border-radius: 50%; background: var(--green); }
  .brand-name { font-size: 34px; font-weight: 700; color: var(--green); letter-spacing: -0.5px; }
  .contact { position: absolute; left: 592px; top: 53px; font-size: 13px; line-height: 16px; color: var(--dark); }
  .contact-name { color: var(--green); font-weight: 700; }
  .contact-role { color: var(--orange); margin-bottom: 7px; }
  .contact-line { display: flex; align-items: center; gap: 4px; }
  .contact-line svg { width: 9px; height: 9px; fill: var(--green); }
  .salutation {
    position: absolute; left: 65px; top: 236px;
    font-family: "Arimo", sans-serif; font-weight: 700; font-size: 18px; color: var(--heading);
  }
  .body-copy { position: absolute; left: 65px; top: 281px; width: 685px; }
  .body-copy p {
    font-size: 16.5px; line-height: 21.4px; color: var(--text);
    text-align: justify; margin-bottom: 21.4px;
  }
  .signature {
    position: absolute; left: 65px; top: 803px; width: 155px; height: 76px;
    background: linear-gradient(135deg, #eeeeee, #dcdcdc); border-radius: 4px;
  }
  .footer {
    position: absolute; left: 0; bottom: 0; width: 816px; height: 38px;
    background: var(--green); color: #fff;
  }
  .footer-address {
    position: absolute; left: 65px; top: 9px; display: flex; align-items: center; gap: 7px;
    font-size: 13px;
  }
  .footer-address strong { font-weight: 700; }
  .footer-address svg { width: 12px; height: 17px; fill: #fff; }
  .web-tab { position: absolute; left: 535px; top: -3px; width: 232px; height: 34px; }
  .web-tab svg { position: absolute; inset: 0; }
  .web-tab span {
    position: absolute; left: 0; right: 0; top: 5px; text-align: center;
    font-size: 13px; font-weight: 700; letter-spacing: 0.8px; color: #fff;
  }
</style>
</head>
<body>
<main class="letter">
  <header>
    <div class="brand"><span class="brand-mark"></span><span class="brand-name">Birchwell Agency</span></div>
    <div class="contact">
      <div class="contact-name">Marcus Hale</div>
      <div class="contact-role">Agency Principal</div>
      <div class="contact-line"><svg viewBox="0 0 10 10"><path d="M2 0.5 L3.8 2.6 L2.9 3.7 Q4 6 6.3 7.1 L7.4 6.2 L9.5 8 L8.4 9.5 Q3.5 9 0.5 1.6 Z"/></svg>555-014-2290</div>
      <div class="contact-line"><svg viewBox="0 0 10 10"><path d="M0 2 H10 V8.5 H0 Z M0 2 L5 5.5 L10 2" stroke="#fff" stroke-width="0.8"/></svg>marcus@birchwellagency.example</div>
    </div>
  </header>

  <h1 class="salutation">Dear Mr. Carter,</h1>

  <section class="body-copy">
    <p>Lorem Ipsum is simply dummy text of the printing and typesetting industry. Lorem Ipsum has been the industry's standard dummy text ever since the 1500s, when an unknown printer took a galley of type and scrambled it to make a type specimen book. It has survived not only five centuries, but also the leap into electronic typesetting, remaining essentially unchanged.</p>
    <p>The standard chunk of Lorem Ipsum used since the 1500s is reproduced below for those interested. Sections 1.10.32 and 1.10.33 from "de Finibus Bonorum et Malorum" by Cicero are also reproduced in their exact original form, accompanied by English versions from the 1914 translation by H. Rackham</p>
    <p>Lorem Ipsum is simply dummy text of the printing and typesetting industry. Lorem Ipsum has been the industry's standard dummy text ever since the 1500s, when an unknown printer took a galley of type and scrambled it to make a type specimen book. It has survived not only five centuries, but also the leap into electronic typesetting, remaining essentially unchanged. It was popularised in the</p>
    <p>Lorem Ipsum is simply dummy text of the printing and typesetting industry. Lorem Ipsum has been the industry's standard dummy text ever since the 1500s, when an unknown printer took a galley of type and scrambled it to make a type specimen book. It has survived not only five centuries, but also the leap into electronic typesetting, remaining essentially unchanged. It was popularised in the</p>
  </section>

  <div class="signature" role="img" aria-label="Handwritten signature of the agency principal"></div>

  <footer class="footer">
    <div class="footer-address">
      <svg viewBox="0 0 12 17"><path d="M6 0 A6 6 0 0 1 12 6 C12 10 6 17 6 17 C6 17 0 10 0 6 A6 6 0 0 1 6 0 Z M6 3.5 A2.5 2.5 0 1 0 6 8.5 A2.5 2.5 0 1 0 6 3.5 Z"/></svg>
      <span><strong>Birchwell Agency, Inc</strong> 742 Lakeview Parkway Ste. 210 Fairhaven, FL 32099</span>
    </div>
    <div class="web-tab">
      <svg viewBox="0 0 232 34" width="232" height="34"><path d="M0 0 H232 L212 26 Q206 34 194 34 H38 Q26 34 20 26 Z" fill="#fff"/><path d="M4 0 H228 L209 24 Q204 31 193 31 H39 Q28 31 23 24 Z" fill="var(--orange)"/></svg>
      <span>www.birchwellagency.example</span>
    </div>
  </footer>
</main>
</body>
</html>
```